Cat Toy Box Design

We are looking to design our packaging for our cat toy. The box is a
6.75 inches x 6.75 inches x 11.75 inches.

The images I've uploaded is from a sample box - We will need to add our logo to it. I have also attached our logo.

```html
<!DOCTYPE html>
<html lang="en">
<head>
<meta charset="utf-8">
<title>Plushpaw Goods – Cat Toy Box Panel</title>
<link rel="stylesheet" href="https://fonts.googleapis.com/css2?family=Arimo:wght@700&display=swap">
<style>
  :root {
    --canvas: #ffffff;
    --panel-edge: #111111;
    --ink: #111111;
    --dot-purple: #9b7fbb;
    --dot-sky: #d4eaf7;
    --dot-orange: #fcb24f;
    --dot-green: #a6d47c;
    --band-navy: #1a4566;
    --band-text: #ffffff;
    --photo-light: #eee9ec;
    --photo-blush: #ecd3d8;
    --photo-warm: #cdb8a6;
    --photo-fur: #a89482;
    --photo-cool: #d5e6ee;
  }
  html, body {
    margin: 0;
    width: 1200px;
    height: 1200px;
    overflow: hidden;
    background: var(--canvas);
  }
  .canvas {
    position: relative;
    width: 1200px;
    height: 1200px;
  }
  .box-panel {
    position: absolute;
    left: 297px;
    top: 89px;
    width: 594px;
    height: 1031px;
    display: block;
  }
  .brand-name,
  .brand-url {
    font-family: "Arimo", Arial, sans-serif;
    font-weight: 700;
    fill: var(--ink);
  }
  .band-url {
    font-family: "Arimo", Arial, sans-serif;
    font-weight: 700;
    fill: var(--band-text);
  }
</style>
</head>
<body>
<main class="canvas">
  <svg class="box-panel" viewBox="0 0 520 902" xmlns="http://www.w3.org/2000/svg">
    <defs>
      <clipPath id="panel-clip">
        <rect x="0" y="0" width="520" height="902"/>
      </clipPath>
      <linearGradient id="photo-tones" x1="0" y1="0" x2="1" y2="1">
        <stop offset="0" stop-color="var(--photo-blush)"/>
        <stop offset="0.35" stop-color="var(--photo-warm)"/>
        <stop offset="0.55" stop-color="var(--photo-light)"/>
        <stop offset="0.75" stop-color="var(--photo-fur)"/>
        <stop offset="1" stop-color="var(--photo-cool)"/>
      </linearGradient>
    </defs>

    <g clip-path="url(#panel-clip)">
      <rect class="panel-ground" x="0" y="0" width="520" height="902" fill="var(--canvas)"/>

      <g class="decor-dots">
        <circle cx="35" cy="52" r="50" fill="var(--dot-purple)"/>
        <circle cx="435" cy="77" r="85" fill="var(--dot-sky)"/>
        <circle cx="80" cy="297" r="82" fill="var(--dot-orange)"/>
        <circle cx="445" cy="317" r="83" fill="var(--dot-green)"/>
      </g>

      <g class="brand-block">
        <text class="brand-name" x="260" y="192" font-size="34" text-anchor="middle" textLength="266" lengthAdjust="spacingAndGlyphs">Plushpaw Goods</text>
        <text class="brand-url" x="260" y="222" font-size="14" text-anchor="middle">www.plushpawgoods.com</text>
      </g>

      <path class="product-photo" role="img"
            aria-label="Photo of a tabby and white kitten lying among colourful felt pom-pom balls"
            d="M0,405 Q260,248 520,405 L520,834 L0,834 Z"
            fill="url(#photo-tones)"/>

      <g class="footer-band">
        <rect x="0" y="834" width="520" height="68" fill="var(--band-navy)"/>
        <text class="band-url" x="260" y="865" font-size="21" text-anchor="middle">www.plushpawgoods.com</text>
      </g>
    </g>

    <rect class="panel-edge" x="0.75" y="0.75" width="518.5" height="900.5"
          fill="none" stroke="var(--panel-edge)" stroke-width="1.5"/>
  </svg>
</main>
</body>
</html>
```